Real estate Agent postcards for homeowners

I need a "Just Sold" postcard for two real agents , I am providing pictures of the agents and neighborhood.
I have the front and back of a postcard containing the information I want on the postcard.
I want a designer to take the info and pictures and design a new postcard and choose the colors

Target Market(s)

homeowners of luxury condos

Industry/Entity Type

Real Estate Agent

Colors

Designer to choose colors to be used in the design.

```html
<!DOCTYPE html>
<html lang="en">
<head>
<meta charset="utf-8">
<title>Just Sold Postcard</title>
<link rel="stylesheet" href="https://fonts.googleapis.com/css2?family=Cormorant+Garamond:wght@400;500;600&family=Pinyon+Script&family=Open+Sans:wght@400&display=swap">
<style>
  :root {
    --card-bg: #8e98ac;
    --ink-dark: #3e4350;
    --text-light: #ffffff;
    --frame: #5f6879;
    --stamp-line: #cbd1dc;
    --divider: #4f5769;
    --scene-top: #c9b08a;
    --scene-bottom: #7f8a9a;
    --portrait-a: #c8a77f;
    --portrait-b: #6c9bc0;
  }
  html, body {
    margin: 0;
    padding: 0;
    width: 1200px;
    height: 851px;
    overflow: hidden;
    background: var(--card-bg);
  }
  .postcard {
    position: relative;
    width: 1200px;
    height: 851px;
    background: var(--card-bg);
    font-family: "Cormorant Garamond", serif;
    color: var(--text-light);
  }
  .neighborhood-strip {
    position: absolute;
    left: 0; top: 0;
    width: 1200px; height: 13px;
    background: linear-gradient(90deg, var(--scene-top), var(--scene-bottom));
  }
  .network-badge {
    position: absolute;
    left: 24px; top: 28px;
    display: flex;
    align-items: center;
    gap: 10px;
    font-family: "Cormorant Garamond", serif;
    font-weight: 600;
    font-size: 24px;
    color: var(--ink-dark);
  }
  .network-badge .mark {
    width: 58px; height: 58px;
    background: var(--ink-dark);
  }
  .stamp-box {
    position: absolute;
    left: 1024px; top: 32px;
    width: 134px; height: 182px;
    border: 3px solid var(--stamp-line);
    box-sizing: border-box;
  }
  .headline {
    position: absolute;
    left: 220px; top: 40px;
    width: 780px;
    margin: 0;
    font-family: "Pinyon Script", cursive;
    font-weight: 400;
    font-size: 64px;
    line-height: 76px;
    text-align: center;
    color: var(--ink-dark);
  }
  .listing {
    position: absolute;
    top: 240px;
    margin: 0;
    font-size: 25px;
    line-height: 45px;
    letter-spacing: 3px;
  }
  .listing--buyer { left: 28px; text-align: left; }
  .listing--seller { right: 48px; text-align: right; }
  .listing strong {
    font-style: italic;
    font-weight: 600;
    font-size: 28px;
  }
  .agent-photo {
    position: absolute;
    top: 428px;
    height: 270px;
    box-sizing: border-box;
    border: 12px solid var(--frame);
  }
  .agent-photo--left {
    left: 21px; width: 205px;
    background: linear-gradient(160deg, var(--portrait-a), #9ec3d4);
  }
  .agent-photo--right {
    left: 962px; width: 206px;
    background: linear-gradient(180deg, var(--portrait-b), #2f5f86);
  }
  .divider {
    position: absolute;
    left: 615px; top: 407px;
    width: 5px; height: 214px;
    background: var(--divider);
  }
  .agent-info {
    position: absolute;
    top: 448px;
    margin: 0;
    font-size: 22px;
    line-height: 36px;
    letter-spacing: 3px;
    font-style: normal;
  }
  .agent-info--left { left: 257px; text-align: left; }
  .agent-info--right { right: 262px; text-align: right; }
  .agent-name { text-transform: uppercase; }
  .brokerage {
    position: absolute;
    left: 0; top: 626px;
    width: 1200px;
    margin: 0;
    text-align: center;
    font-weight: 500;
    font-size: 35px;
    letter-spacing: 6px;
    text-transform: uppercase;
  }
  .call-to-action {
    position: absolute;
    left: 0; top: 670px;
    width: 1200px;
    margin: 0;
    text-align: center;
    font-family: "Pinyon Script", cursive;
    font-size: 42px;
    color: var(--ink-dark);
  }
  .office {
    position: absolute;
    left: 0; top: 738px;
    width: 1200px;
    margin: 0;
    text-align: center;
    font-family: "Open Sans", sans-serif;
    font-size: 25px;
    line-height: 38px;
    font-style: normal;
    letter-spacing: 0.5px;
  }
</style>
</head>
<body>
<main class="postcard">
  <div class="neighborhood-strip" role="img" aria-label="Photograph of the condo neighborhood"></div>

  <div class="network-badge">
    <span class="mark"></span>
    <span>Brokers Network</span>
  </div>

  <div class="stamp-box"></div>

  <h1 class="headline">We're local agents and your neighbors.</h1>

  <p class="listing listing--buyer">
    43 Costa Verde in Building 13<br>
    3 bedrooms, 2 bathrooms, 1,840 sq. ft<br>
    Sold for <strong>$1,000,000</strong> buys side.
  </p>

  <p class="listing listing--seller">
    80 Costa Verde in building 8<br>
    1 bedroom, 2 bathrooms, 985 sq. ft<br>
    Sold for <strong>$7698, 000</strong> seller side.
  </p>

  <div class="agent-photo agent-photo--left" role="img" aria-label="Portrait of agent Laura Penrose"></div>

  <address class="agent-info agent-info--left">
    <span class="agent-name">Laura Penrose</span><br>
    (310) 555 - 0148<br>
    HomesbyLaura@example.com<br>
    Unit 24-15
  </address>

  <div class="divider"></div>

  <address class="agent-info agent-info--right">
    <span class="agent-name">Theo Marlow</span><br>
    (650) 555 - 0192<br>
    TheoMarlow@example.com<br>
    UNIT 6-37
  </address>

  <div class="agent-photo agent-photo--right" role="img" aria-label="Portrait of agent Theo Marlow by the sea"></div>

  <h2 class="brokerage">Harbor Crest Realtors</h2>
  <p class="call-to-action">Call us!</p>

  <address class="office">
    57 Coral Lane, Bayview, CA 90210 - 1234<br>
    Visit us at www.harborcrestrealtors.com
  </address>
</main>
</body>
</html>
```